THE WELLNESS BARN WEBSITE for Physio, Fitness, health

An attractive website advertising a physiotherapyand fitness / gym business, not generic, colours are natural, greens, browns, beiges. No cheesy pictures. With the ability to sell a small,amount of goods online if i decide to. Simple to navigate. Text boxes that i can input the main information and change easily. Somewhere to put my timetable. Easy to find contact details. However many pages it needs, im not fussed.
Target Market(s)
People looking for rehabilitation or fitness classes
Industry/Entity Type
Physiotherapy, Fitness, Gym, Health
Coding
Coded - Design and coding required
Number of Pages Required
1 page
Font styles to use
Other font styles liked:
- Im not fusse,ld, not script
Requirements
Must have
- Will upload posts from my business insta page for reference about the feel. Earthy natural tones, I have a lot of timber, and rustic looking piece's, plants etc in my clinic
Nice to have
- Simple to navigate
Should not have
- Cheesy "yoga" or generic "people doing physio" pics

```html
<!DOCTYPE html>
<html lang="en">
<head>
<meta charset="utf-8">
<title>The Wellness Barn</title>
<link href="https://fonts.googleapis.com/css2?family=Josefin+Sans:wght@300;400;600;700&family=Montserrat:wght@600;700&display=swap" rel="stylesheet">
<style>
  :root {
    --timber: #8f6a4b;
    --timber-light: #a88462;
    --beige: #c7b494;
    --sage: #8ea27d;
    --moss: #6f8a63;
    --nav-bg: rgba(246, 239, 226, 0.72);
    --nav-active: rgba(255, 252, 245, 0.75);
    --nav-line: #5a4636;
    --ink: #1b1510;
    --brand-green: #1f3a1c;
    --headline: rgba(255, 251, 242, 0.96);
    --btn-light: #fffdf8;
    --btn-soft: rgba(248, 242, 230, 0.85);
    --btn-border: #d6cbb8;
  }
  * { box-sizing: border-box; margin: 0; padding: 0; }
  html, body { width: 1200px; height: 675px; overflow: hidden; }
  body { position: relative; font-family: 'Josefin Sans', sans-serif; color: var(--ink); }

  .hero-visual {
    position: absolute; inset: 0;
    background:
      radial-gradient(ellipse 55% 60% at 30% 55%, rgba(70, 48, 30, 0.28), transparent 70%),
      radial-gradient(ellipse at 75% 35%, rgba(255, 248, 232, 0.22), transparent 60%),
      linear-gradient(100deg, var(--timber) 0%, var(--timber-light) 28%, var(--beige) 55%, var(--sage) 82%, var(--moss) 100%);
  }

  .site-nav {
    position: absolute; top: 0; left: 0; width: 1200px; height: 34px;
    background: var(--nav-bg);
    display: flex; align-items: stretch;
    padding-left: 380px;
  }
  .site-nav a {
    font-family: 'Montserrat', sans-serif; font-weight: 700;
    font-size: 8px; letter-spacing: 0.12em; color: var(--ink);
    text-decoration: none; display: flex; align-items: center;
    padding: 0 10px;
  }
  .site-nav a.is-active {
    background: var(--nav-active);
    border-bottom: 2px solid var(--nav-line);
    width: 60px; padding: 2px 0 0 12px;
  }
  .site-nav a.is-active + a { padding-left: 6px; }

  .brand-name {
    position: absolute; left: 141px; top: 40px;
    font-family: 'Josefin Sans', sans-serif; font-weight: 700;
    font-size: 31px; line-height: 34px; letter-spacing: 0.02em;
    color: var(--brand-green);
  }

  .hero-copy { position: absolute; left: 135px; top: 210px; }
  .tagline {
    font-weight: 400; font-size: 22px; color: var(--ink);
  }
  .headline {
    margin-top: 12px;
    font-weight: 700; font-size: 59px; line-height: 62px;
    letter-spacing: 0.01em; color: var(--headline);
  }

  .hero-actions { position: absolute; left: 129px; top: 432px; display: flex; gap: 9px; }
  .btn {
    height: 46px; display: flex; align-items: center; justify-content: center;
    font-family: 'Montserrat', sans-serif; font-weight: 700; font-size: 11.5px;
    letter-spacing: 0.12em; color: var(--ink); text-decoration: none;
    border: 2px solid var(--btn-border); border-radius: 6px;
  }
  .btn-primary { width: 175px; background: var(--btn-light); }
  .btn-secondary { width: 133px; background: var(--btn-soft); }
</style>
</head>
<body>
  <div class="hero-visual" role="img" aria-label="Warm clinic interior with timber, rustic pieces and plants"></div>

  <nav class="site-nav">
    <a href="#" class="is-active">ABOUT</a>
    <a href="#">SERVICES</a>
    <a href="#">LAKESIDE</a>
    <a href="#">RETREAT</a>
    <a href="#">TOOL</a>
    <a href="#">KIT</a>
  </nav>

  <div class="brand-name">THE<br>WELLNESS<br>BARN</div>

  <section class="hero-copy">
    <p class="tagline">your home of Holistic Health and Wellness</p>
    <h1 class="headline">SIMPLE TOOLS FOR<br>LIVING YOUR BEST<br>LIFE</h1>
  </section>

  <div class="hero-actions">
    <a href="#" class="btn btn-primary">VIEW DEPARTMENT</a>
    <a href="#" class="btn btn-secondary">CONTACT US</a>
  </div>
</body>
</html>
```